Cedar Gate Labradoodle web design

We're a new labradoodle breeder in Charleston, SC in need of a web design.

Our name is Cedar Gate Labradoodles.

Site we like: http://www.pebblefernlabradoodles.example/
http://www.quintbrookdoodles.example/

Logo Font:
The ''Cedar Gate'' font is called TestarossaNF and is available freely at http://www.typevatsample.example/veltrano-kx.font.  The ''Labradoodles'' font is called Worstveld Sling Extra and is available freely at http://www.glyphcrateonline.example/BrimholtDashHeavy.php.

Requirements
Must have
• Our logo
1. Home page
2. Labradoodle F.A.Q.
3. Our doodles
4. Availability
5. Adoption Process
6. Contact us
Link/badge icon for Health Guarantee
Nice to have
• Color and font to match the logo.

An area to add pictures
Should not have
• Rainbows
Rainbow colors

```html
<!DOCTYPE html>
<html lang="en">
<head>
<meta charset="utf-8">
<title>Cedar Gate Labradoodles</title>
<link rel="stylesheet" href="https://fonts.googleapis.com/css2?family=Cinzel+Decorative:wght@700;900&family=Dosis:wght@500;600&family=PT+Sans:wght@400;700&display=swap">
<style>
:root{
  --ink:#111;
  --pink:#f27a98;
  --pink-deep:#e8194f;
  --pink-soft:#f7a3bc;
  --crimson:#c8173f;
  --orange:#ef9a2e;
  --orange-soft:#f8c27a;
  --grey:#8a8a8a;
  --grey-soft:#c9c9c9;
  --text:#555;
  --paper:#f1f1f1;
}
*{box-sizing:border-box;margin:0;padding:0}
html,body{width:1200px;height:1198px;overflow:hidden}
body{position:relative;background:#fff;font-family:"PT Sans",Verdana,sans-serif;color:var(--text)}
.abs{position:absolute}

.top-band{left:0;top:0;width:1200px;height:98px;background:repeating-linear-gradient(45deg,#1e1e1e 0 2px,#151515 2px 4px)}
.top-band::before{content:"";position:absolute;left:0;top:0;width:100%;height:5px;background:radial-gradient(circle at 4px 0,var(--pink) 4px,transparent 4.5px) 0 0/8px 5px repeat-x}
.top-rule{left:0;top:98px;width:1200px;height:5px;background:var(--pink)}

.main-nav{left:160px;top:53px;display:flex;gap:7px}
.main-nav a{display:block;height:45px;line-height:48px;padding:0 18px;background:#fff;border-radius:14px 14px 0 0;
  font-family:"Cinzel Decorative",serif;font-weight:700;font-size:14.5px;color:var(--pink);text-decoration:none;white-space:nowrap}
.main-nav a.is-current{background:var(--pink);color:#fff;padding:0 30px}

.brand{left:160px;top:128px;width:250px;height:220px;display:flex;flex-direction:column;align-items:center;justify-content:center;gap:14px}
.brand-mark{width:90px;height:90px;border-radius:50%;background:var(--pink)}
.brand-name{font-family:"PT Sans",sans-serif;font-weight:700;font-size:22px;color:var(--crimson);text-align:center;line-height:1.2}

.hero-photo{left:620px;top:118px;width:470px;height:432px;border-radius:40% 40% 30% 30%;
  background:radial-gradient(ellipse at 50% 45%,#efe2c8 0%,#f6eee0 55%,#fff 78%)}

.tagline{left:163px;top:376px;font-family:"Cinzel Decorative",serif;font-weight:900;color:#3a3a3a;line-height:1;white-space:nowrap}
.tagline .line-one{display:block;font-size:34px}
.tagline .line-two{display:block;margin:14px 0 0 100px;font-size:44px;color:var(--ink)}
.tagline .line-two em{font-style:normal;color:var(--crimson)}

.hero-button{left:376px;top:493px;width:246px;height:42px;border-radius:21px;background:linear-gradient(#555,#1f1f1f);
  color:#fff;font-family:"Dosis",sans-serif;font-weight:500;font-size:20px;text-align:center;line-height:42px}

.feature{top:572px;width:268px;height:220px;border-radius:18px;padding:20px 20px;color:#fff}
.feature h2{font-family:"Cinzel Decorative",serif;font-weight:900;font-size:21px;color:#fff;text-shadow:1px 1px 1px #333;margin-bottom:16px;white-space:nowrap}
.feature .lead{font-weight:700;font-size:12.5px;line-height:1.2;margin-bottom:13px}
.feature p{font-size:12px;line-height:1.2}
.feature .more{position:absolute;right:18px;bottom:20px;width:118px;height:28px;border-radius:14px;
  font-family:"Cinzel Decorative",serif;font-weight:700;font-size:13px;color:#fff;text-align:center;line-height:29px;text-shadow:1px 1px 1px #555}
.feature--welcome{left:159px;background:linear-gradient(160deg,var(--pink-soft),var(--pink-deep) 70%);border:1px solid #d9144a}
.feature--welcome .more{background:linear-gradient(var(--pink-soft),var(--pink-deep))}
.feature--doodles{left:467px;background:linear-gradient(160deg,var(--orange-soft),var(--orange) 70%);color:#3a2510}
.feature--doodles h2{color:#3a2510;text-shadow:none}
.feature--doodles .more{background:linear-gradient(#fbd27a,#f0a82a)}
.feature--adoption{left:772px;width:270px;background:linear-gradient(160deg,var(--grey-soft),var(--grey) 70%)}
.feature--adoption h2{font-size:19px;letter-spacing:-0.3px}
.feature--adoption ul{list-style:none;font-size:13px;line-height:21px}
.feature--adoption li{display:flex;align-items:center;gap:8px}
.feature--adoption .more{background:linear-gradient(#f2f2f2,#a8a8a8)}

.lower-field{left:0;top:830px;width:1200px;height:258px;background:linear-gradient(#fff,var(--paper) 30%)}

.about{left:158px;top:862px;width:565px}
.about h1{font-family:"Cinzel Decorative",serif;font-weight:900;font-size:23px;color:var(--ink);white-space:nowrap}
.about .lead{margin-top:12px;font-weight:700;font-size:13px;color:var(--crimson)}
.about p.body{margin-top:10px;font-size:12.5px;line-height:19.5px;color:#777}
.about .more{display:inline-block;margin-top:16px;margin-left:-2px;width:99px;height:28px;border-radius:14px;background:#333;color:var(--orange);font-size:12px;text-align:center;line-height:28px}

.newsletter{left:771px;top:859px;width:264px;height:168px;border:1px solid #ddd;border-radius:18px;background:#fff;padding:14px 19px}
.newsletter h2{font-family:"Cinzel Decorative",serif;font-weight:900;font-size:19px;color:var(--orange);margin-top:4px}
.newsletter p{margin-top:12px;font-size:12px;line-height:1.2;color:#444}
.signup{display:flex;margin-top:22px;height:28px;border-radius:14px;overflow:hidden}
.signup span{flex:1;background:#666;color:#fff;font-size:12px;line-height:28px;padding-left:18px}
.signup b{width:49px;background:linear-gradient(var(--orange-soft),#e07f12);color:#fff;font-family:"Cinzel Decorative",serif;font-size:15px;text-align:center;line-height:28px}

.footer{left:0;top:1088px;width:1200px;height:110px;background:repeating-linear-gradient(45deg,#1e1e1e 0 2px,#151515 2px 4px)}
.footer::before{content:"";position:absolute;left:0;top:0;width:100%;height:6px;background:radial-gradient(circle at 5px 0,#fff 5px,transparent 5.5px) 0 0/10px 6px repeat-x}
.footer-nav{left:164px;top:1126px;font-size:12px;color:#999}
.footer-nav a{color:#999;text-decoration:none}
.footer-nav .sep{margin:0 19px}
.copyright{left:164px;top:1151px;font-size:12px;color:#ddd}
.social{left:839px;top:1145px;display:flex;gap:6px}
.social span{width:26px;height:26px;border-radius:50%;background:#3a6fc1}
.social span:nth-child(2){background:#c9352b}
.social span:nth-child(3){background:#1e7ec1}
.footer-brand{left:945px;top:1112px;width:100px;text-align:center;display:flex;flex-direction:column;align-items:center;gap:5px}
.footer-brand i{width:34px;height:34px;border-radius:50%;background:#888}
.footer-brand span{font-weight:700;font-size:11px;color:#ccc;line-height:1.1}
</style>
</head>
<body>
  <div class="abs top-band"></div>
  <div class="abs top-rule"></div>

  <nav class="abs main-nav">
    <a class="is-current" href="#">Home</a>
    <a href="#">FAQ</a>
    <a href="#">Our Doodles</a>
    <a href="#">Availability</a>
    <a href="#">Adoption Process</a>
    <a href="#">Contact Us</a>
  </nav>

  <div class="abs brand">
    <div class="brand-mark"></div>
    <div class="brand-name">Cedar Gate<br>Labradoodles</div>
  </div>

  <div class="abs hero-photo" role="img" aria-label="Photo of two cream labradoodle puppies sitting side by side"></div>

  <h2 class="abs tagline">
    <span class="line-one">A DOG WILL LOVE</span>
    <span class="line-two">YOU <em>FOREVER !</em></span>
  </h2>
  <div class="abs hero-button">Learn more about Doodles</div>

  <section class="abs feature feature--welcome">
    <h2>Welcome</h2>
    <p class="lead">Lorem Ipsum is simply dummy text of the printing and typesetting industry.</p>
    <p>Lorem Ipsum has been the industry's standard dummy text ever since the 1500s, when an unknown printer took a galley of type and scrambled it to make</p>
    <span class="more">Read More</span>
  </section>

  <section class="abs feature feature--doodles">
    <h2>Our Doodles</h2>
    <p class="lead">Lorem Ipsum is simply dummy text of the printing and typesetting industry.</p>
    <p>Lorem Ipsum has been the industry's standard dummy text ever since the 1500s, when an unknown printer took a galley of type and scrambled it to make</p>
    <span class="more">Read More</span>
  </section>

  <section class="abs feature feature--adoption">
    <h2>Adoption Process</h2>
    <ul>
      <li><svg width="18" height="16" viewBox="0 0 18 16"><path d="M2 9l5 5L16 2" fill="none" stroke="#fff" stroke-width="3" stroke-linecap="round"/></svg>Lorem Ipsum has been</li>
      <li><svg width="18" height="16" viewBox="0 0 18 16"><path d="M2 9l5 5L16 2" fill="none" stroke="#fff" stroke-width="3" stroke-linecap="round"/></svg>standard dummy text ever since</li>
      <li><svg width="18" height="16" viewBox="0 0 18 16"><path d="M2 9l5 5L16 2" fill="none" stroke="#fff" stroke-width="3" stroke-linecap="round"/></svg>the 1500s, when</li>
      <li><svg width="18" height="16" viewBox="0 0 18 16"><path d="M2 9l5 5L16 2" fill="none" stroke="#fff" stroke-width="3" stroke-linecap="round"/></svg>galley of type and scrambled it</li>
    </ul>
    <span class="more">Read More</span>
  </section>

  <div class="abs lower-field"></div>

  <section class="abs about">
    <h1>Cedar Gate Labradoodles</h1>
    <p class="lead">Lorem Ipsum is simply dummy text of the printing and typesetting industry.</p>
    <p class="body">Lorem Ipsum is simply dummy text of the printing and typesetting industry. Lorem Ipsum has been the industry's standard dummy text ever since the 1500s, when an unknown printer took a galley of type and scrambled it to makeLorem Ipsum is simply dummy text of the printing and typesetting industry. Lorem Ipsum has been the industry's standard dummy text ever since the 1500s.</p>
    <span class="more">Read More »</span>
  </section>

  <section class="abs newsletter">
    <h2>Newsletters</h2>
    <p>Lorem Ipsum is simply dummy text of the printing and typesetting industry.</p>
    <div class="signup"><span>Enter your e-mail here</span><b>Go !</b></div>
  </section>

  <footer class="abs footer"></footer>
  <div class="abs footer-nav">
    <a href="#">Home</a><span class="sep">|</span><a href="#">FAQ</a><span class="sep">|</span><a href="#">Our Doodles</a><span class="sep">|</span><a href="#">Availability</a><span class="sep">|</span><a href="#">Adoption Process</a><span class="sep">|</span><a href="#">Contact Us</a>
  </div>
  <div class="abs copyright">Copyright © 2013 ~ All Rights Reserved Cedar Gate Labradoodles</div>
  <div class="abs social" aria-label="Social links"><span></span><span></span><span></span></div>
  <div class="abs footer-brand"><i></i><span>Cedar Gate<br>Labradoodles</span></div>
</body>
</html>
```